Brightkoru NZ Brand, Revenue, Promotions & Events

I need an innovative business card that pops my brand. I like the colours against darker gradients and i'm not afraid to be bold.

I run my own Business, Brand, Event & Promotion company. I specialise in breathing life into businesses and adding atmosphere to promotions and events. I am concept based lady that likes to test the boundaries and create stand out campaigns that connect with the consumer.

I have 12 years business experience in a realm of interesting fields form 11 years in coordinating international music festivals & promotions, 6 years in radio with 8 radio awards including a NZ radio award for best sales team in NZ and was the national brand and sales manager for New Zealands 1st indoor entertainment mall. With 10 years of experience in advertising sales, I have an eye for creating revenue streams for businesses and thrive on implementing campaigns that compliment those streams.

I love sayings like "Do what you love, love what you do" and believe that you can achieve anything you want.

I have been fortunate in my career that my connections have carried me without needing to promote my business however it is important that I start to do so.

Target Market(s)

Decision makers 25 to 54

Contact Information for Business Card

Petra Holsworth
Director
p. 022 739 5081
e. petra@brightkoru.example
www.brightkoru.example

FB, IG and Linkedin logo

Font styles to use
Sans Serif

Colors

Designer to choose colors to be used in the design.

Requirements
Must have
• Petra Holsworth
• Director
• p. 022 739 5081
• e. petra@brightkoru.example
• www.brightkoru.example
• FB, IG and Linkedin logo
Nice to have
• I am looking for a business card with character, that leaves my presence with my customer and makes them remember my brand & optimistic personality when i walk out the door.

```html
<!DOCTYPE html>
<html lang="en">
<head>
<meta charset="utf-8">
<title>Brightkoru NZ Business Card</title>
<link href="https://fonts.googleapis.com/css2?family=Montserrat:wght@500;600;700&family=Arimo:wght@400&display=swap" rel="stylesheet">
<style>
  :root {
    --brand-blue: #1fa8e0;
    --ink-grey: #555555;
    --paper: #ffffff;
    --edge: #222222;
  }
  * { margin: 0; padding: 0; box-sizing: border-box; }
  html, body {
    width: 1200px; height: 1200px; overflow: hidden;
    background: var(--paper);
  }
  .canvas { position: relative; width: 1200px; height: 1200px; }
  .card {
    position: absolute; left: 237px; width: 709px; height: 433px;
    box-shadow: 14px 16px 14px rgba(0,0,0,0.22);
    overflow: hidden;
  }
  .card-front { top: 137px; background: var(--brand-blue); }
  .card-back { top: 633px; background: var(--paper); border: 1px solid var(--edge); }

  .wordmark {
    font-family: "Montserrat", sans-serif; font-weight: 500;
    letter-spacing: 0.06em; white-space: nowrap; line-height: 1;
  }
  .tagline {
    font-family: "Arimo", Arial, sans-serif; font-weight: 400;
    white-space: nowrap; line-height: 1;
  }

  .card-front .wordmark {
    position: absolute; left: 0; right: 0; top: 178px;
    text-align: center; font-size: 58px; color: var(--paper);
  }
  .card-front .tagline {
    position: absolute; left: 0; right: 0; top: 241px;
    text-align: center; font-size: 24px; color: var(--paper);
  }

  .card-back .wordmark {
    position: absolute; left: 38px; top: 74px;
    font-size: 40px; color: var(--brand-blue);
  }
  .card-back .tagline {
    position: absolute; left: 38px; top: 124px;
    font-size: 17px; color: var(--ink-grey);
  }
  .contact-band {
    position: absolute; left: 0; top: 216px; width: 100%; height: 217px;
    background: var(--brand-blue);
  }
  .person-name {
    position: absolute; left: 51px; top: 243px;
    font-family: "Montserrat", sans-serif; font-weight: 700;
    font-size: 30px; color: var(--ink-grey); white-space: nowrap;
  }
  .person-title {
    position: absolute; left: 50px; top: 283px;
    font-family: "Montserrat", sans-serif; font-weight: 500;
    font-size: 21px; color: var(--paper); letter-spacing: 0.02em;
  }
  .contact-row {
    position: absolute; left: 49px; display: flex; align-items: center; gap: 10px;
    font-family: "Montserrat", sans-serif; font-weight: 700;
    font-size: 19px; color: var(--paper); white-space: nowrap;
  }
  .contact-row svg { display: block; flex: none; }
  .row-phone { top: 313px; }
  .row-email { top: 345px; }
  .row-web { top: 374px; }
  .row-web .web-label { font-size: 21px; width: 28px; }
  .row-web .web-address { color: var(--ink-grey); }
  .social-links {
    position: absolute; left: 516px; top: 360px; display: flex; gap: 10px;
  }
  .social-slot {
    width: 33px; height: 33px; border: 3px solid var(--paper); border-radius: 4px;
  }
</style>
</head>
<body>
<main class="canvas">
  <section class="card card-front" aria-label="Card front">
    <div class="wordmark">BRIGHTKORU NZ</div>
    <div class="tagline">BRAND | REVENUE | EVENTS &amp; PROMOTIONS</div>
  </section>

  <section class="card card-back" aria-label="Card back">
    <div class="wordmark">BRIGHTKORU NZ</div>
    <div class="tagline">BRAND | REVENUE | EVENTS &amp; PROMOTIONS</div>
    <div class="contact-band"></div>

    <h1 class="person-name">Petra Holsworth</h1>
    <p class="person-title">Director</p>

    <div class="contact-row row-phone">
      <svg width="20" height="26" viewBox="0 0 20 26" aria-hidden="true">
        <rect x="2" y="1.5" width="16" height="23" rx="3" fill="none" stroke="#fff" stroke-width="2.5"/>
        <circle cx="10" cy="21" r="1.6" fill="#fff"/>
      </svg>
      <span>022 739 5081</span>
    </div>
    <div class="contact-row row-email">
      <svg width="24" height="18" viewBox="0 0 24 18" aria-hidden="true">
        <rect x="1.2" y="1.2" width="21.6" height="15.6" fill="none" stroke="#fff" stroke-width="2.2"/>
        <path d="M1.5 1.5 L12 10 L22.5 1.5 M1.5 16.5 L9 8.5 M22.5 16.5 L15 8.5" fill="none" stroke="#fff" stroke-width="2"/>
      </svg>
      <span>petra@brightkoru.example</span>
    </div>
    <div class="contact-row row-web">
      <span class="web-label">W</span>
      <span class="web-address">www.brightkoru.example</span>
    </div>

    <div class="social-links" aria-label="Social profiles">
      <div class="social-slot"></div>
      <div class="social-slot"></div>
      <div class="social-slot"></div>
    </div>
  </section>
</main>
</body>
</html>
```